Vietnam Motorcycle Trip TRAVEL GUIDE!! Book Cover!

I need an adventurous book cover for a book called "THROTTLE SAGA: A Drifter's Handbook to Crossing the Spine of Vietnam". I would like people to look at the cover and think adventure and Vietnam. I want it to appeal to backpackers and people who have not travelled to Vietnam. A motorbike riding along a road in Vietnam would be ideal with some landscapes to suggest we are definitely in Vietnam. The rear cover could perhaps be one of Vietnam's tropical beaches or something else that says "this place is a paradise". It could also be something else that is quinessentially Vietnamese.

The book will be A5 Dimensions. And it will also need a printable A5 interior cover too. The interior covers can just be images. No text needed. These interior images can be motorcycle related or Vietnam related. Perhaps some images of Vietnam or some Pho or Banh Mi to give it a bit of flavour. Or a long open road with a motorbike on it.

Please leave space in the external rear, lower right hand corner for a barcode.

I've attached some images to gain inspiration from. And a sample chapter.

Colours I'd like to see on there - greens, camoflague perhaps, yellow, brown, blue.

Target Market(s)

Male backpackers aged 18-35 years old. New Zealand and Australian travellers.

Font styles to use
Serif
Sans Serif

Requirements
Must have
• Exterior and Interior covers.
Barcode space.
Title and subtitle.
Synopsis on rear cover.
Exciting title fonts - perhaps Brushstroke or something equally exciting and rugged
Nice to have
• Colours I'd like to see on there - greens, camoflague perhaps, yellow, brown, blue.

A motorbike riding on the open road of Vietnam.

Rice paddies, beaches, Vietnam War stuff perhaps.

A New Zealand Flag
A Vietnam Flag
Should not have
• Scenery from countries outside Southeast Asia

```html
<!DOCTYPE html>
<html lang="en">
<head>
<meta charset="utf-8">
<title>Throttle Saga — Book Cover</title>
<link rel="stylesheet" href="https://fonts.googleapis.com/css2?family=Big+Shoulders+Display:wght@800&family=Josefin+Sans:wght@400;600;700&family=Yellowtail&display=swap">
<style>
  :root {
    --paper: #ffffff;
    --cover-black: #1f1f1f;
    --saga-yellow: #f2b21f;
    --subtitle-white: #f4f4f2;
    --hill-green: #6f8f3c;
    --hill-dark: #3f5a26;
    --road-grey: #b7b0aa;
    --haze: #d9d6cc;
  }
  * { margin: 0; padding: 0; box-sizing: border-box; }
  html, body {
    width: 871px; height: 1200px; overflow: hidden;
    background: var(--paper);
  }
  .cover {
    position: absolute;
    left: 44px; top: 44px;
    width: 783px; height: 1112px;
    background: var(--cover-black);
  }
  .cover-photo {
    position: absolute;
    left: 125px; top: 116px;
    width: 533px; height: 464px;
    background:
      linear-gradient(200deg, var(--haze) 0%, rgba(217,214,204,0) 30%),
      radial-gradient(ellipse at 80% 82%, var(--road-grey) 0%, rgba(183,176,170,0) 40%),
      linear-gradient(160deg, var(--hill-dark) 0%, var(--hill-green) 45%, #8aa253 70%, #9c9a86 100%);
  }
  .title-mark {
    position: absolute;
    left: 125px; top: 590px;
    width: 533px; height: 250px;
    display: block;
  }
  .title-word {
    font-family: "Big Shoulders Display", "Arial Narrow", sans-serif;
    font-weight: 800;
    font-size: 250px;
  }
  .series-word {
    position: absolute;
    left: 125px; top: 860px;
    width: 533px;
    display: flex; justify-content: space-between;
    font-family: "Josefin Sans", sans-serif;
    font-weight: 700;
    font-size: 72px;
    line-height: 1;
    color: var(--saga-yellow);
  }
  .subtitle {
    position: absolute;
    left: 0; top: 960px; width: 100%;
    text-align: center;
    font-family: "Josefin Sans", sans-serif;
    font-weight: 600;
    font-size: 16px;
    letter-spacing: 0.4px;
    color: var(--subtitle-white);
  }
  .author {
    position: absolute;
    left: 0; top: 995px; width: 100%;
    text-align: center;
    font-family: "Yellowtail", cursive;
    font-size: 34px;
    color: var(--saga-yellow);
  }
</style>
</head>
<body>
  <main class="cover">
    <div class="cover-photo" role="img" aria-label="Winding mountain road through green hills in northern Vietnam with small motorbike riders on the hairpin bends"></div>

    <svg class="title-mark" viewBox="0 0 533 250" aria-label="Throttle">
      <defs>
        <linearGradient id="title-fill" x1="0" y1="0" x2="1" y2="1">
          <stop offset="0" stop-color="#7d9a48"/>
          <stop offset="0.45" stop-color="#b9b3ab"/>
          <stop offset="0.7" stop-color="#8aa253"/>
          <stop offset="1" stop-color="#c4beb6"/>
        </linearGradient>
      </defs>
      <text class="title-word" x="0" y="222" textLength="533" lengthAdjust="spacingAndGlyphs"
            fill="url(#title-fill)" stroke="#2a2a20" stroke-width="1.2">THROTTLE</text>
    </svg>

    <h1 class="series-word" aria-label="Saga"><span>S</span><span>A</span><span>G</span><span>A</span></h1>

    <p class="subtitle">A DRIFTER'S HANDBOOK TO CROSSING THE SPINE OF VIETNAM</p>
    <p class="author">Callum Westbrook</p>
  </main>
</body>
</html>
```